Innovative Event Ticketing Start Up. Needs a Web Design

We need a web design for a new company based in London called 'Mavrolet'. We are a platform which facilitates the building of groups of customers for events. As more people commit to an event, the price incrementally decreases. We would like there to be an emphasis on the sharing element and the decreasing price with higher participation.

Any quieres please email me at rkdw47@mailbarn.net

Target Market(s)

18-30 year olds who are active and savvy across social media sites

Industry/Entity Type

Events

Number of Pages Required

3 page

Other font styles liked:
• Phi Roman

Requirements
Must have
• Each event offering runs for a limited time so a countdown timer is also to be included as well as a counter of number of participants (please find example attached).
• The interface needs to have the options for 'Live 'Music', 'Nightlife', 'Festivals', 'Comedy' and 'Everything Else'. Also
• A 'featured' section, for our promoted events
• Social sharing icons for Facebook, Twitter, WhatsApp, SMS and Email
• Room the inclusion of a video
• Pages for clients to sign up - registering details ect.
• Content is still being completed, so room available to add when ready
Nice to have
• An interface design we like as a guiding templates on is https://quorvexapp.com/
• Zelo wordpress theme is also of interest.
• Scroll over clicking for main interface and also for the event once clicked upon.
• Event pages similar desgin to quorvex with same features such as Google Maps but also participant counter and affiliate marketing options.
Should not have
• CMS no longer necessary

```html
<!DOCTYPE html>
<html lang="en">
<head>
<meta charset="utf-8">
<title>Mavrolet — Events</title>
<link rel="stylesheet" href="https://fonts.googleapis.com/css2?family=Oswald:wght@400;500;600&family=Open+Sans:wght@400;600;700&display=swap">
<style>
:root{
  --red:#e0222b;
  --red-dark:#b8141c;
  --ink:#1f1f1f;
  --text:#555;
  --muted:#8a8a8a;
  --line:#e4e4e4;
  --paper:#ffffff;
  --soft:#f3f3f3;
  --grey-band:#ececec;
}
*{box-sizing:border-box;margin:0;padding:0}
html,body{width:1200px;height:3988px;overflow:hidden}
body{font-family:"Open Sans",Arial,sans-serif;color:var(--text);background:var(--paper);font-size:13px;line-height:1.6}
h1,h2,h3,h4,.oswald{font-family:"Oswald","Arial Narrow",sans-serif;font-weight:500;color:var(--ink);text-transform:uppercase}
.wrap{width:1000px;margin:0 auto;position:relative}
.btn{display:inline-block;font-family:"Oswald","Arial Narrow",sans-serif;text-transform:uppercase;font-size:13px;letter-spacing:.5px;padding:0 26px;height:36px;line-height:36px;background:var(--red);color:#fff}
.btn.ghost{background:#fff;color:var(--red);border:1px solid var(--red);line-height:34px}

/* header / hero */
.hero{position:relative;height:660px;overflow:hidden;color:#fff;text-align:center}
.hero-photo{position:absolute;inset:0;background:radial-gradient(ellipse at 50% 40%,#e2485a 0%,#b1243a 45%,#5a1220 100%)}
.hero-shade{position:absolute;inset:0;background:linear-gradient(180deg,rgba(120,10,25,.35),rgba(60,5,15,.45))}
.nav{position:absolute;top:0;left:0;right:0;height:90px;z-index:2}
.nav .wrap{display:flex;align-items:center;height:90px}
.brand{display:flex;align-items:center;gap:10px;font-family:"Oswald",sans-serif;font-size:26px;font-weight:500;color:#fff;letter-spacing:1px}
.brand-mark{width:26px;height:26px;background:#fff}
.menu{display:flex;margin-left:auto;height:90px}
.menu a{font-family:"Oswald",sans-serif;font-size:12px;color:#fff;text-transform:uppercase;padding:0 22px;line-height:90px;height:90px}
.menu a.active{background:var(--red)}
.social{display:flex;gap:10px;margin-left:24px}
.social span{width:12px;height:12px;border-radius:50%;background:#fff}
.hero-body{position:relative;z-index:2;padding-top:170px}
.hero h1{color:#fff;font-size:62px;font-weight:600;letter-spacing:1px;line-height:1.1}
.hero-lead{width:640px;margin:26px auto 0;font-size:14px;line-height:1.7;color:#fbe3e6;text-transform:uppercase;letter-spacing:.5px}
.countdown{display:flex;justify-content:center;gap:18px;margin-top:40px}
.count{width:82px;text-align:center}
.count b{display:block;height:70px;line-height:70px;background:rgba(25,25,25,.7);font-family:"Oswald",sans-serif;font-size:40px;font-weight:500;color:#fff}
.count i{display:block;font-style:normal;background:var(--red);font-family:"Oswald",sans-serif;font-size:11px;line-height:22px;text-transform:uppercase}
.hero .btn{margin-top:44px;padding:0 40px;height:44px;line-height:44px}

/* welcome */
.welcome{height:460px;padding-top:110px}
.welcome .wrap{display:flex;justify-content:space-between}
.welcome-copy{width:440px}
.welcome h2{font-size:26px;margin-bottom:24px}
.welcome p{font-size:12px;margin-bottom:16px;color:var(--muted)}
.welcome .actions{display:flex;gap:18px;margin-top:28px}
.video{width:480px;height:290px;background:#16171c;position:relative;margin-top:-10px}
.video-still{position:absolute;left:0;right:0;top:32px;bottom:46px;background:linear-gradient(180deg,#2a3348 0%,#3f4d6b 45%,#1c2230 100%)}
.video-title{position:absolute;top:0;left:0;right:0;height:32px;line-height:32px;padding-left:14px;font-family:"Oswald",sans-serif;font-size:12px;color:#ddd}
.video-bar{position:absolute;left:0;right:0;bottom:0;height:46px;display:flex;align-items:center;padding:0 14px;gap:14px}
.video-track{flex:1;height:4px;background:#555;position:relative}
.video-track::before{content:"";position:absolute;left:0;top:0;bottom:0;width:38%;background:var(--red)}

/* section head */
.section-head{display:flex;align-items:center;gap:20px;margin-bottom:48px}
.section-icon{width:60px;height:60px;background:var(--red);display:flex;align-items:center;justify-content:center}
.section-head h2{font-size:26px}
.section-head p{font-size:12px;color:var(--muted);line-height:1.5}

/* events */
.events{height:880px;background:var(--grey-band);padding-top:72px}
.event-grid{display:grid;grid-template-columns:repeat(3,320px);gap:28px 20px}
.event-card{background:#fff;height:272px}
.event-media{display:flex;height:184px}
.event-date{width:36px;background:#fff;display:flex;align-items:center;justify-content:center}
.event-date span{transform:rotate(-90deg);white-space:nowrap;font-family:"Oswald",sans-serif;font-size:11px;color:var(--ink)}
.event-photo{flex:1}
.event-info{display:flex;height:88px;padding:10px 0 0 12px}
.event-meta{flex:1}
.event-meta h3{font-family:"Open Sans",sans-serif;text-transform:none;color:var(--red);font-size:14px;font-weight:600;margin-bottom:6px}
.event-meta p{font-size:10px;color:var(--muted);line-height:1.9}
.price{width:66px;height:78px;margin-top:-10px;background:var(--red);color:#fff;text-align:center;font-family:"Oswald",sans-serif}
.price.plain{background:#fff;color:var(--muted)}
.price b{display:block;font-size:26px;font-weight:500;line-height:52px}
.price i{display:block;font-style:normal;font-size:10px;border-top:1px solid rgba(255,255,255,.4);line-height:26px}
.price.plain i{border-color:var(--line)}
.events .center{text-align:center;margin-top:44px}

/* features */
.features{height:760px;padding-top:100px}
.feature-row{display:flex;justify-content:center;gap:70px}
.feature-row + .feature-row{margin-top:70px}
.feature{width:280px;text-align:center}
.feature svg{display:block;margin:0 auto 22px}
.feature h4{font-size:15px;margin-bottom:10px}
.feature p{font-size:11px;color:var(--muted);line-height:1.7}
.feature a{display:block;font-size:11px;color:var(--red);margin-top:2px}

/* promoted */
.promoted{height:640px;background:var(--grey-band);padding-top:56px}
.promoted .section-head{margin-bottom:36px}
.promo-strip{display:flex;height:380px}
.promo{flex:1;position:relative}
.promo-tag{position:absolute;top:0;right:20px;background:var(--red);color:#fff;font-family:"Oswald",sans-serif;font-size:11px;padding:2px 12px}
.promo-name{position:absolute;left:0;right:0;bottom:0;height:34px;line-height:34px;text-align:center;color:#fff;font-family:"Oswald",sans-serif;font-size:15px;text-transform:uppercase;background:rgba(0,0,0,.45)}
.promo-name.hot{background:var(--red)}
.dots{display:flex;justify-content:center;gap:8px;margin-top:24px}
.dots span{width:30px;height:4px;background:#cfcfcf}
.dots span.on{background:var(--red)}

/* partners */
.partners{height:248px;display:flex;align-items:center}
.partners .wrap{display:flex;justify-content:space-between;align-items:center}
.partner{width:110px;height:56px;display:flex;align-items:center;justify-content:center}
.partner span{background:#c7c7c7}

/* footer */
.footer{height:300px;background:var(--red);color:#fff;padding-top:38px}
.footer .wrap{display:flex}
.footer-about{width:340px}
.footer-about .brand{font-size:24px;margin-bottom:16px}
.footer-about p{font-size:11px;line-height:1.7;color:#fde0e1;margin-bottom:10px}
.footer-col{width:190px}
.footer-col h4{color:#fff;font-size:15px;margin-bottom:14px}
.footer-col li{list-style:none;font-size:11px;line-height:2;color:#fde0e1}
.query{width:280px}
.query h4{color:#fff;font-size:15px;margin-bottom:14px}
.field{height:24px;background:#fff;margin-bottom:8px;font-size:10px;color:var(--muted);padding-left:8px;line-height:24px}
.field.area{height:54px}
.query .submit{height:26px;background:var(--ink);color:#fff;font-family:"Oswald",sans-serif;font-size:11px;text-align:center;line-height:26px}
.copyright{height:48px;background:var(--red-dark);color:#fde0e1;font-size:11px;text-align:center;line-height:48px}
</style>
</head>
<body>

<header class="hero">
  <div class="hero-photo" role="img" aria-label="Concert crowd with raised hands under red stage lights"></div>
  <div class="hero-shade"></div>
  <nav class="nav">
    <div class="wrap">
      <div class="brand"><span class="brand-mark"></span>MAVROLET</div>
      <div class="menu">
        <a class="active">Home</a><a>About</a><a>Schedule</a><a>Events</a><a>Sponsors</a><a>Gallery</a><a>Contact</a>
      </div>
      <div class="social"><span></span><span></span><span></span></div>
    </div>
  </nav>
  <div class="hero-body">
    <h1>Our Latest Event Is Ready Now</h1>
    <p class="hero-lead">Join the crowd early, share it with your friends and watch the ticket price drop as more people sign up for the night</p>
    <div class="countdown">
      <div class="count"><b>04</b><i>Days</i></div>
      <div class="count"><b>12</b><i>Hours</i></div>
      <div class="count"><b>34</b><i>Minutes</i></div>
      <div class="count"><b>52</b><i>Seconds</i></div>
    </div>
    <a class="btn">Register Now</a>
  </div>
</header>

<section class="welcome">
  <div class="wrap">
    <div class="welcome-copy">
      <h2>Welcome to Mavrolet</h2>
      <p>Mavrolet brings people together around the events they love. Every event runs for a limited time, and the more friends who commit, the lower the price gets for everyone in the group.</p>
      <p>Pick a night out, share it across your favourite channels and follow the participant counter as it climbs. Live music, nightlife, festivals, comedy and everything else, all in one place.</p>
      <div class="actions"><a class="btn">Get Tickets</a><a class="btn ghost">Program</a></div>
    </div>
    <div class="video">
      <div class="video-title">MAVROLET — YOUR NIGHT STARTS HERE</div>
      <div class="video-still" role="img" aria-label="Video still of a city skyline at dusk"></div>
      <div class="video-bar">
        <svg width="14" height="14" viewBox="0 0 14 14"><rect x="2" y="1" width="3" height="12" fill="#fff"/><rect x="9" y="1" width="3" height="12" fill="#fff"/></svg>
        <div class="video-track"></div>
        <svg width="16" height="14" viewBox="0 0 16 14"><path d="M1 5h4l4-4v12l-4-4H1z" fill="#fff"/></svg>
      </div>
    </div>
  </div>
</section>

<section class="events">
  <div class="wrap">
    <div class="section-head">
      <div class="section-icon"><svg width="30" height="30" viewBox="0 0 30 30"><rect x="3" y="6" width="24" height="21" fill="none" stroke="#fff" stroke-width="2.5"/><rect x="3" y="6" width="24" height="6" fill="#fff"/><rect x="8" y="2" width="3" height="7" fill="#fff"/><rect x="19" y="2" width="3" height="7" fill="#fff"/><rect x="11" y="16" width="8" height="7" fill="#fff"/></svg></div>
      <div><h2>New Events by Mavrolet</h2><p>Fresh events added every week. Commit early, invite your crew and pay less together.</p></div>
    </div>
    <div class="event-grid">
      <article class="event-card">
        <div class="event-media"><div class="event-date"><span>12 JUNE</span></div><div class="event-photo" role="img" aria-label="Stage show with blue lights" style="background:linear-gradient(135deg,#1d5fd1,#5fb6f0 55%,#1a2f8a)"></div></div>
        <div class="event-info"><div class="event-meta"><h3>Your Event Name</h3><p>08:00 PM – 11:30 PM</p><p>London Event Venue</p></div><div class="price"><b>$45</b><i>BUY NOW</i></div></div>
      </article>
      <article class="event-card">
        <div class="event-media"><div class="event-date"><span>18 JUNE</span></div><div class="event-photo" role="img" aria-label="Fashion runway show" style="background:linear-gradient(135deg,#2b2a30,#7a6a66 55%,#1d1c22)"></div></div>
        <div class="event-info"><div class="event-meta"><h3>Your Event Name</h3><p>08:00 PM – 11:30 PM</p><p>London Event Venue</p></div><div class="price"><b>$39</b><i>BUY NOW</i></div></div>
      </article>
      <article class="event-card">
        <div class="event-media"><div class="event-date"><span>24 JUNE</span></div><div class="event-photo" role="img" aria-label="Performers on a lit stage" style="background:linear-gradient(135deg,#0f7fcf,#59c1f2 50%,#2b4f8c)"></div></div>
        <div class="event-info"><div class="event-meta"><h3>Your Event Name</h3><p>08:00 PM – 11:30 PM</p><p>London Event Venue</p></div><div class="price plain"><b>$15</b><i>FULL</i></div></div>
      </article>
      <article class="event-card">
        <div class="event-media"><div class="event-date"><span>02 JULY</span></div><div class="event-photo" role="img" aria-label="Comedy night performer in costume" style="background:linear-gradient(135deg,#c8262b,#f0b13a 50%,#7a1a1a)"></div></div>
        <div class="event-info"><div class="event-meta"><h3>Your Event Name</h3><p>08:00 PM – 11:30 PM</p><p>London Event Venue</p></div><div class="price"><b>$05</b><i>BUY NOW</i></div></div>
      </article>
      <article class="event-card">
        <div class="event-media"><div class="event-date"><span>09 JULY</span></div><div class="event-photo" role="img" aria-label="Singer on a dark stage" style="background:linear-gradient(135deg,#111,#4a4d58 55%,#0b0b10)"></div></div>
        <div class="event-info"><div class="event-meta"><h3>Your Event Name</h3><p>08:00 PM – 11:30 PM</p><p>London Event Venue</p></div><div class="price"><b>$50</b><i>BUY NOW</i></div></div>
      </article>
      <article class="event-card">
        <div class="event-media"><div class="event-date"><span>15 JULY</span></div><div class="event-photo" role="img" aria-label="Festival crowd at sunset" style="background:linear-gradient(135deg,#f2b23a,#d97a24 50%,#4a2a14)"></div></div>
        <div class="event-info"><div class="event-meta"><h3>Your Event Name</h3><p>08:00 PM – 11:30 PM</p><p>London Event Venue</p></div><div class="price"><b>$19</b><i>BUY NOW</i></div></div>
      </article>
    </div>
    <div class="center"><a class="btn">View More</a></div>
  </div>
</section>

<section class="features">
  <div class="feature-row">
    <div class="feature">
      <svg width="56" height="56" viewBox="0 0 56 56"><circle cx="28" cy="18" r="11" fill="#222"/><path d="M8 54c0-13 9-20 20-20s20 7 20 20z" fill="#222"/><path d="M14 19a14 14 0 0 1 28 0" fill="none" stroke="#222" stroke-width="3"/></svg>
      <h4>Booking Tickets Easily</h4>
      <p>Reserve your place in a few taps, invite friends and see the price fall as the group grows.</p><a>Read More</a>
    </div>
    <div class="feature">
      <svg width="56" height="56" viewBox="0 0 56 56"><rect x="20" y="4" width="16" height="30" rx="8" fill="#222"/><path d="M13 26a15 15 0 0 0 30 0" fill="none" stroke="#222" stroke-width="3"/><rect x="26.5" y="40" width="3" height="10" fill="#222"/><rect x="18" y="49" width="20" height="3" fill="#222"/></svg>
      <h4>Listen Live Musics</h4>
      <p>Gigs, club nights and festivals from across the city, all gathered together in one simple feed.</p><a>Read More</a>
    </div>
    <div class="feature">
      <svg width="56" height="56" viewBox="0 0 56 56"><path d="M14 36a10 10 0 0 1 2-20 13 13 0 0 1 25-2 11 11 0 0 1 1 22z" fill="#222"/><path d="M28 36v14M20 44v6M36 44v6" stroke="#222" stroke-width="3"/></svg>
      <h4>Quick Connections</h4>
      <p>Share events on every channel you use and bring your whole crew along for a better price.</p><a>Read More</a>
    </div>
  </div>
  <div class="feature-row">
    <div class="feature">
      <svg width="56" height="56" viewBox="0 0 56 56"><path d="M28 4l20 7v15c0 13-9 22-20 26C17 48 8 39 8 26V11z" fill="#222"/><path d="M19 28l7 7 12-13" fill="none" stroke="#fff" stroke-width="4"/></svg>
      <h4>100% Customer Service</h4>
      <p>Our London team is on hand to help with bookings, refunds and anything else you need.</p><a>Read More</a>
    </div>
    <div class="feature">
      <svg width="56" height="56" viewBox="0 0 56 56"><g fill="#222"><circle cx="20" cy="22" r="11"/><g stroke="#222" stroke-width="5"><path d="M20 6v32M4 22h32M9 11l22 22M31 11L9 33"/></g><circle cx="40" cy="40" r="8"/><g stroke="#222" stroke-width="4"><path d="M40 28v24M28 40h24"/></g></g><circle cx="20" cy="22" r="4" fill="#fff"/><circle cx="40" cy="40" r="3" fill="#fff"/></svg>
      <h4>Listen Live Musics</h4>
      <p>Discover new artists every week and get first access to limited time group offers.</p><a>Read More</a>
    </div>
  </div>
</section>

<section class="promoted">
  <div class="wrap">
    <div class="section-head">
      <div class="section-icon"><svg width="30" height="30" viewBox="0 0 30 30"><rect x="3" y="6" width="24" height="21" fill="none" stroke="#fff" stroke-width="2.5"/><rect x="3" y="6" width="24" height="6" fill="#fff"/><rect x="8" y="2" width="3" height="7" fill="#fff"/><rect x="19" y="2" width="3" height="7" fill="#fff"/><rect x="11" y="16" width="8" height="7" fill="#fff"/></svg></div>
      <div><h2>Promoted Events by Mavrolet</h2><p>Featured picks from our partners, hand selected for this month.</p></div>
    </div>
  </div>
  <div class="promo-strip">
    <div class="promo" role="img" aria-label="Black and white concert hall crowd" style="background:linear-gradient(160deg,#6a6a6a,#2a2a2a)"><span class="promo-tag">MUSIC</span><div class="promo-name">Event Name Here</div></div>
    <div class="promo" role="img" aria-label="Singer performing with a microphone" style="background:linear-gradient(160deg,#a08a70,#4a3a2c)"><span class="promo-tag">LIVE</span><div class="promo-name hot">Event Name Here</div></div>
    <div class="promo" role="img" aria-label="Black and white comedy performer" style="background:linear-gradient(160deg,#8a8a8a,#333)"><span class="promo-tag">COMEDY</span><div class="promo-name">Event Name Here</div></div>
    <div class="promo" role="img" aria-label="Black and white fashion runway" style="background:linear-gradient(160deg,#9a9a9a,#3a3a3a)"><span class="promo-tag">NIGHTLIFE</span><div class="promo-name">Event Name Here</div></div>
  </div>
  <div class="dots"><span class="on"></span><span></span><span></span></div>
</section>

<section class="partners">
  <div class="wrap">
    <div class="partner"><span style="width:44px;height:44px;border-radius:50%"></span></div>
    <div class="partner"><span style="width:40px;height:40px;border-radius:50%"></span></div>
    <div class="partner"><span style="width:42px;height:42px"></span></div>
    <div class="partner"><span style="width:44px;height:44px;border-radius:50%"></span></div>
    <div class="partner"><span style="width:46px;height:40px"></span></div>
    <div class="partner"><span style="width:40px;height:40px;border-radius:50%"></span></div>
  </div>
</section>

<footer class="footer">
  <div class="wrap">
    <div class="footer-about">
      <div class="brand"><span class="brand-mark"></span>MAVROLET</div>
      <p>Mavrolet is a London platform for building groups around events. The more people who commit, the lower the price for all.</p>
      <p>Questions? Write to us at rkdw47@mailbarn.net and our team will get back to you soon.</p>
    </div>
    <div class="footer-col"><h4>Quick Links</h4><ul><li>Home</li><li>About</li><li>Schedule</li><li>Events</li><li>Sponsors</li><li>Gallery</li><li>Contact</li></ul></div>
    <div class="footer-col"><h4>Services</h4><ul><li>Booking Tickets</li><li>Live Musics</li><li>Easy To Pay</li><li>Customer Service</li></ul></div>
    <div class="query">
      <h4>Send Query</h4>
      <div class="field">Name</div>
      <div class="field">Email</div>
      <div class="field area">Message</div>
      <div class="submit">SUBMIT</div>
    </div>
  </div>
</footer>
<div class="copyright">The Mavrolet. Copyright All Rights Reserved</div>

</body>
</html>
```